Yogurt business needs packaging designs for spout pouch and boxes

We are launching a new yogurt brand and seeking a talented designer to create a packaging materials that are modern, eye-catching, and appealing to families and health-conscious consumers. The designs should convey freshness, fun, and premium quality.

Scope of Work:
Yogurt Pouch Design: Primary packaging design for yogurt pouches (multiple flavors).

Box Packaging Design: Secondary packaging design for multipack boxes (to hold multiple pouches).

Create a cohesive visual identity across all materials.

Include space for nutritional facts, barcode, regulatory details, and flavor differentiation.

Ensure designs align with FMCG retail standards and stand out on supermarket shelves.

Style & Inspiration:

Fresh, natural, and playful with clean, modern typography.

Bright and colorful palettes adaptable by flavor (e.g., strawberry, Mango, blueberry, vanilla,natural).

Approachable, family-friendly style inspired by Brackenmoor, HopSip Curdlies, and Willowbeck Dairy pouch yogurt.

Deliverables:

Print-ready packaging designs for pouches and boxes.

Editable source files for future updates.

3D mockups to visualize the designs on real packaging.

Target Audience:

Families with children.

Young, health-conscious consumers seeking nutritious and tasty snacks.

Brand Keywords:
Fresh • Natural • Healthy • Fun • Premium

*use of AI is permitted if justified in the design

Target Market(s)

please refer to creative brief document attached

Industry/Entity Type

Yoghurt/Food & Beverage

Requirements
Must have
• please refer to creative brief document attached
Nice to have

```html
<!DOCTYPE html>
<html lang="en">
<head>
<meta charset="utf-8">
<title>Spoonly Strawberry – Multipack Dieline and Pouch</title>
<link rel="stylesheet" href="https://fonts.googleapis.com/css2?family=Baloo+2:wght@700;800&family=Inter:wght@400;600;700&display=swap">
<style>
  :root {
    --paper: #ffffff;
    --red: #d93d3b;
    --red-panel: #d44341;
    --red-fold: #c93533;
    --red-deep: #b52c2b;
    --berry: #c22a2e;
    --leaf: #4f9a3c;
    --cream: #f5f1ea;
    --cream-shade: #e4dccf;
    --white: #ffffff;
    --ink-light: rgba(255,255,255,0.85);
  }
  html, body {
    margin: 0;
    padding: 0;
    width: 1200px;
    height: 1000px;
    overflow: hidden;
    background: var(--paper);
  }
  .artboard { display: block; width: 1200px; height: 1000px; }
  .panel { fill: var(--red-panel); }
  .panel-fold { fill: var(--red-fold); }
  .panel-edge { stroke: var(--red-deep); stroke-width: 0.4; }
  .brand-name { font-family: "Baloo 2", sans-serif; font-weight: 800; fill: var(--white); }
  .tagline { font-family: "Baloo 2", sans-serif; font-weight: 700; fill: var(--white); }
  .flavour { font-family: "Baloo 2", sans-serif; font-weight: 700; fill: var(--white); }
  .fine-print { font-family: "Inter", sans-serif; font-weight: 400; fill: var(--ink-light); }
  .fine-bold { font-family: "Inter", sans-serif; font-weight: 700; fill: var(--white); }
  .rule { stroke: var(--ink-light); stroke-width: 0.3; }
  .count-numeral { font-family: "Inter", sans-serif; font-weight: 700; fill: var(--white); }
  .badge-shape { fill: none; stroke: var(--ink-light); stroke-width: 0.5; }
  .fruit-art { fill: var(--berry); opacity: 0.55; }
  .code-box { fill: var(--white); }
  .window-frame { fill: var(--white); }
  .pouch-body { fill: var(--red); }
  .pouch-cap { fill: var(--cream); stroke: var(--cream-shade); stroke-width: 1; }
  .claim-badge { fill: var(--red); stroke: var(--white); stroke-width: 2; }
  .claim-text { font-family: "Baloo 2", sans-serif; font-weight: 800; fill: var(--white); }
</style>
</head>
<body>
<svg class="artboard" viewBox="0 0 1200 1000" xmlns="http://www.w3.org/2000/svg">
  <defs>
    <linearGradient id="window-fill" x1="0" y1="0" x2="0" y2="1">
      <stop offset="0" stop-color="#d9453f"/>
      <stop offset="0.6" stop-color="#d9453f"/>
      <stop offset="1" stop-color="#f3ede4"/>
    </linearGradient>
    <linearGradient id="splash-fill" x1="0" y1="0" x2="0" y2="1">
      <stop offset="0" stop-color="#f7f4ee"/>
      <stop offset="1" stop-color="#e9e2d6"/>
    </linearGradient>
    <clipPath id="pouch-clip">
      <path d="M950,424 Q950,410 964,410 H1040 L1058,386 H1094 L1112,410 H1116 Q1130,410 1130,424 V696 Q1130,710 1116,710 H964 Q950,710 950,696 Z"/>
    </clipPath>
  </defs>

  <!-- Multipack carton dieline -->
  <g class="carton-dieline" transform="translate(-402,115) scale(1.5)">

    <!-- glue flap and side panels, left -->
    <path class="panel-fold panel-edge" d="M328,187 L295,200 V300 L328,312 Z"/>
    <rect class="panel panel-edge" x="328" y="187" width="57" height="125"/>
    <rect class="panel-fold panel-edge" x="385" y="187" width="45" height="125"/>

    <!-- nutrition panel with dust flaps -->
    <path class="panel-fold panel-edge" d="M430,180 L448,157 H505 L523,180 Z"/>
    <rect class="panel panel-edge" x="430" y="180" width="93" height="135"/>
    <path class="panel-fold panel-edge" d="M430,315 L448,342 H505 L523,315 Z"/>

    <!-- top tuck and top panel -->
    <path class="panel panel-edge" d="M523,125 V60 L531,50 H622 L630,60 V125 Z"/>
    <rect class="panel-fold panel-edge" x="523" y="125" width="107" height="55"/>

    <!-- front panel -->
    <rect class="panel panel-edge" x="523" y="180" width="107" height="135"/>

    <!-- bottom panels -->
    <rect class="panel-fold panel-edge" x="523" y="315" width="107" height="30"/>
    <rect class="panel panel-edge" x="523" y="345" width="107" height="65"/>
    <path class="panel-fold panel-edge" d="M523,410 H630 V432 L622,440 H531 L523,432 Z"/>

    <!-- info panel with dust flaps -->
    <path class="panel-fold panel-edge" d="M630,180 L648,157 H707 L725,180 Z"/>
    <rect class="panel panel-edge" x="630" y="180" width="95" height="135"/>
    <path class="panel-fold panel-edge" d="M630,315 L648,342 H707 L725,315 Z"/>

    <!-- side panels and flap, right -->
    <rect class="panel-fold panel-edge" x="725" y="187" width="45" height="125"/>
    <rect class="panel panel-edge" x="770" y="187" width="58" height="125"/>
    <path class="panel-fold panel-edge" d="M828,187 L860,200 V300 L828,312 Z"/>

    <!-- front panel artwork -->
    <g class="front-face">
      <g role="img" aria-label="Strawberry and leaf illustrations around the panel edges">
        <ellipse class="fruit-art" cx="528" cy="236" rx="6" ry="8"/>
        <ellipse class="fruit-art" cx="626" cy="196" rx="5" ry="7"/>
        <ellipse class="fruit-art" cx="530" cy="292" rx="6" ry="7"/>
        <ellipse class="fruit-art" cx="625" cy="262" rx="5" ry="7"/>
        <ellipse class="fruit-art" cx="534" cy="187" rx="5" ry="5"/>
      </g>
      <text class="brand-name" x="576.5" y="203" font-size="17" text-anchor="middle">Spoonly</text>
      <text class="tagline" x="576.5" y="215" font-size="6.2" text-anchor="middle">I'm Real Yogurt on the go</text>
      <text class="tagline" x="576.5" y="223" font-size="6.2" text-anchor="middle">with probotic</text>
      <rect class="window-frame" x="540" y="238" width="73" height="53" rx="6"/>
      <rect x="544" y="242" width="65" height="45" rx="4" fill="url(#window-fill)" role="img" aria-label="Two strawberry yogurt pouches seen through the carton window"/>
      <text class="flavour" x="576.5" y="301" font-size="6.5" text-anchor="middle">Strawberry</text>
      <rect class="code-box" x="563" y="304" width="27" height="8"/>
    </g>

    <!-- nutrition panel artwork -->
    <g class="nutrition-face">
      <text class="fine-bold" x="437" y="192" font-size="5">Nutrition Facts</text>
      <text class="fine-print" x="437" y="198" font-size="2.6">Serving Size 1 Pouch (57g)</text>
      <line class="rule" x1="437" y1="201" x2="516" y2="201"/>
      <g class="nutrition-rows" font-size="2.6">
        <text class="fine-print" x="437" y="206">Calories</text><text class="fine-print" x="516" y="206" text-anchor="end">70</text>
        <line class="rule" x1="437" y1="208" x2="516" y2="208"/>
        <text class="fine-print" x="437" y="212">Total Fat</text><text class="fine-print" x="516" y="212" text-anchor="end">1g</text>
        <line class="rule" x1="437" y1="214" x2="516" y2="214"/>
        <text class="fine-print" x="437" y="218">Sodium</text><text class="fine-print" x="516" y="218" text-anchor="end">35mg</text>
        <line class="rule" x1="437" y1="220" x2="516" y2="220"/>
        <text class="fine-print" x="437" y="224">Total Carbs</text><text class="fine-print" x="516" y="224" text-anchor="end">12g</text>
        <line class="rule" x1="437" y1="226" x2="516" y2="226"/>
        <text class="fine-print" x="437" y="230">Total Sugars</text><text class="fine-print" x="516" y="230" text-anchor="end">9g</text>
        <line class="rule" x1="437" y1="232" x2="516" y2="232"/>
        <text class="fine-print" x="437" y="236">Protein</text><text class="fine-print" x="516" y="236" text-anchor="end">3g</text>
        <line class="rule" x1="437" y1="238" x2="516" y2="238"/>
        <text class="fine-print" x="437" y="242">Calcium</text><text class="fine-print" x="516" y="242" text-anchor="end">10%</text>
        <line class="rule" x1="437" y1="244" x2="516" y2="244"/>
      </g>
      <text class="fine-print" x="437" y="250" font-size="2.4">Keep refrigerated. Best before date on top.</text>
      <text class="count-numeral" x="438" y="301" font-size="13">6</text>
      <text class="fine-print" x="438" y="307" font-size="2.6">POUCHES</text>
    </g>

    <!-- info panel artwork -->
    <g class="info-face" font-size="2.6">
      <text class="fine-print" x="636" y="190">Ingredients: cultured pasteurized milk, sugar, strawberry puree,</text>
      <text class="fine-print" x="636" y="195">modified corn starch, pectin, natural flavor, vitamin D3,</text>
      <text class="fine-print" x="636" y="200">live and active yogurt cultures. Contains milk.</text>
      <text class="fine-print" x="636" y="210">Freeze, thaw or enjoy chilled straight from the pouch.</text>
      <text class="fine-print" x="636" y="215">Squeeze gently and twist the cap closed after use.</text>
      <text class="fine-print" x="636" y="225">Made with care by the Spoonly Dairy team.</text>
      <g class="certification-badges">
        <rect class="badge-shape" x="641" y="264" width="10" height="8"/>
        <rect class="badge-shape" x="655" y="264" width="10" height="8"/>
        <circle class="badge-shape" cx="677" cy="268" r="5"/>
        <circle class="badge-shape" cx="647" cy="283" r="5"/>
        <circle class="badge-shape" cx="660" cy="283" r="5"/>
        <circle class="badge-shape" cx="673" cy="283" r="5"/>
        <circle class="badge-shape" cx="686" cy="283" r="5"/>
      </g>
      <g role="img" aria-label="Strawberry illustrations along the panel edges">
        <ellipse class="fruit-art" cx="634" cy="300" rx="5" ry="6"/>
        <ellipse class="fruit-art" cx="719" cy="305" rx="5" ry="6"/>
      </g>
    </g>
  </g>

  <!-- Single spout pouch, flat -->
  <g class="spout-pouch">
    <rect class="pouch-cap" x="1060" y="352" width="32" height="34" rx="3"/>
    <rect class="pouch-cap" x="1056" y="378" width="40" height="8" rx="2"/>
    <path class="pouch-body" d="M950,424 Q950,410 964,410 H1040 L1058,386 H1094 L1112,410 H1116 Q1130,410 1130,424 V696 Q1130,710 1116,710 H964 Q950,710 950,696 Z"/>
    <g clip-path="url(#pouch-clip)">
      <path d="M940,600 Q980,560 1020,590 Q1060,620 1100,580 Q1125,560 1140,575 V720 H940 Z" fill="url(#splash-fill)" role="img" aria-label="Yogurt splash with fresh strawberries"/>
      <g role="img" aria-label="Strawberry and leaf illustration">
        <ellipse class="fruit-art" cx="1000" cy="420" rx="14" ry="10"/>
        <ellipse class="fruit-art" cx="1028" cy="600" rx="14" ry="16"/>
        <ellipse class="fruit-art" cx="1110" cy="690" rx="12" ry="13"/>
      </g>
    </g>
    <text class="brand-name" x="1040" y="475" font-size="34" text-anchor="middle">Spoonly</text>
    <text class="tagline" x="1040" y="497" font-size="11" text-anchor="middle">I'm Real Yogurt on the go</text>
    <text class="tagline" x="1040" y="510" font-size="11" text-anchor="middle">with probotic</text>
    <circle class="claim-badge" cx="1096" cy="548" r="24"/>
    <text class="claim-text" x="1096" y="542" font-size="6" text-anchor="middle">PROBIOTICS</text>
    <text class="claim-text" x="1096" y="550" font-size="6" text-anchor="middle">FOR GUT</text>
    <text class="claim-text" x="1096" y="558" font-size="6" text-anchor="middle">HEALTH</text>
    <rect x="1024" y="674" width="36" height="14" fill="#ffffff" stroke="#d8cfc2" stroke-width="1"/>
  </g>
</svg>
</body>
</html>
```